Website for an electrical contractor :)

We are after a web site which can show pictures of our jobs and our capability in a professional, creative and easily understood way.

----- Brightmoor Electrical ------

We really want a visually good looking website with three sections

Section one:
'Completed projects'
We have a few pictures of jobs which we've completed and would like to show off with a brief description. (see uploads)

Section two:
'Our capabilities'
Just a list of what services we offer

Section three:
We would like a 'contact us' section which people can send us a short msg and upload a file for plans to be able to send to us. We would need their name, phone number and email details. We would also need a short privacy policy saying 'we do not disclose information to third parties'.
We also want to display our contact number and postal address

Good luck :)

Target Market(s)

Adults 25 years+
Business owners
Builders
Real estate agents

Industry/Entity Type

Electrical

Colors

Designer to choose colors to be used in the design.

Requirements
Must have
• Visually appealing
Easy to understand
In the 'Completed projects' section, must have a list for each project we do i can upload pictures for it.

```html
<!DOCTYPE html>
<html lang="en">
<head>
<meta charset="utf-8">
<title>Brightmoor Electrical</title>
<link rel="stylesheet" href="https://fonts.googleapis.com/css2?family=Dosis:wght@300;400;500&family=Cabin:wght@400;500&display=swap">
<style>
:root{
  --red:#e01e26;
  --red-dark:#b3121a;
  --red-soft:#e8434a;
  --ink:#333;
  --grey:#777;
  --line:#e2e2e2;
  --footer:#222323;
  --field:#2e2f30;
  --white:#fff;
}
*{box-sizing:border-box;margin:0;padding:0}
html,body{width:851px;height:1200px;overflow:hidden;background:var(--white)}
body{position:relative;font-family:"Dosis",sans-serif;color:var(--ink)}
.abs{position:absolute}

/* header */
.site-header{position:absolute;left:0;top:0;width:851px;height:48px;background:var(--white)}
.brand{position:absolute;left:143px;top:6px;display:flex;align-items:center;gap:8px;font-family:"Cabin",sans-serif;font-size:28px;color:#444;line-height:1}
.brand-dot{width:14px;height:14px;border-radius:50%;background:var(--red)}
.main-nav{position:absolute;top:0;left:468px;height:48px;display:flex;font-family:"Cabin",sans-serif;font-size:11.5px;color:#333}
.main-nav a{display:block;height:48px;line-height:48px;padding:0 10px;color:inherit;text-decoration:none;border-left:1px solid var(--line)}
.main-nav a:first-child{border-left:none;line-height:46px}

/* hero */
.hero{position:absolute;left:0;top:48px;width:851px;height:309px;background:linear-gradient(160deg,#b8121b 0%,#d6262e 40%,#c31820 70%,#9e0f16 100%)}
.hero-title{position:absolute;left:0;width:874px;top:103px;text-align:center;color:var(--white);font-weight:400;font-size:41px;line-height:53px;letter-spacing:.5px}
.btn-outline{position:absolute;left:337px;top:219px;width:167px;height:45px;border:1px solid rgba(255,255,255,.85);color:var(--white);font-size:15px;font-weight:500;text-align:center;line-height:43px;letter-spacing:.5px}
.notch-up{position:absolute;left:407px;top:342px;width:0;height:0;border-left:14px solid transparent;border-right:14px solid transparent;border-bottom:15px solid var(--white)}

.section-title{position:absolute;left:0;width:851px;text-align:center;color:var(--red);font-weight:400;font-size:25px;letter-spacing:.3px}

/* gallery */
.tile{position:absolute}
.tile-feature{left:0;top:421px;width:301px;height:229px;background:linear-gradient(135deg,#e2404a,#d52a33 60%,#c8222a)}
.tile-a{left:303px;top:421px;width:206px;height:114px;background:linear-gradient(180deg,#6d6a66,#9a958d 70%,#b3ab9f)}
.tile-b{left:512px;top:421px;width:156px;height:114px;background:linear-gradient(160deg,#8a7a6a,#5e5149 60%,#7a6d62)}
.tile-c{left:671px;top:421px;width:180px;height:114px;background:linear-gradient(180deg,#3b3a37,#5a5651 60%,#8a847a)}
.tile-text{left:303px;top:538px;width:315px;height:112px;background:var(--red-soft);color:var(--white);font-family:"Cabin",sans-serif;font-size:10.5px;line-height:13.5px;text-align:center;padding:35px 30px 0}
.tile-d{left:621px;top:538px;width:230px;height:112px;background:linear-gradient(180deg,#7a7064,#a39685 55%,#6a6058)}

/* services */
.service{position:absolute;width:160px;text-align:center;font-size:12.5px;color:var(--grey);font-weight:400}
.service svg{display:block;margin:0 auto 9px}
.btn-red{position:absolute;left:371px;top:898px;width:110px;height:25px;background:var(--red);color:var(--white);font-size:13px;font-weight:500;text-align:center;line-height:25px}

/* footer */
.site-footer{position:absolute;left:0;top:950px;width:851px;height:187px;background:var(--footer)}
.notch-down{position:absolute;left:413px;top:950px;width:0;height:0;border-left:14px solid transparent;border-right:14px solid transparent;border-top:15px solid var(--white)}
.field{position:absolute;background:var(--field);color:#7d7d7d;font-family:"Cabin",sans-serif;font-size:10px;padding:7px 15px}
.btn-send{position:absolute;left:118px;top:1085px;width:363px;height:23px;background:var(--red);color:var(--white);font-family:"Cabin",sans-serif;font-size:11px;text-align:center;line-height:23px}
.contact-line{position:absolute;left:517px;display:flex;align-items:center;color:var(--white);font-family:"Cabin",sans-serif;font-size:10.5px}
.contact-line svg{width:12px;height:12px;margin-right:13px}
.social{position:absolute;top:1082px;width:28px;height:28px;border-radius:50%;background:var(--red)}

.legal-bar{position:absolute;left:0;top:1137px;width:851px;height:63px;background:var(--red);color:var(--white);text-align:center;font-family:"Cabin",sans-serif}
.legal-note{font-size:8px;margin-top:10px}
.copyright{font-size:11px;margin-top:6px}
</style>
</head>
<body>

<header class="site-header">
  <div class="brand"><span class="brand-dot"></span>Brightmoor</div>
  <nav class="main-nav">
    <a>Home</a><a>About us</a><a>Our services</a><a>Contact us</a>
  </nav>
</header>

<section class="hero" role="img" aria-label="Photo of a paved residential driveway beside brick units, tinted red">
  <h1 class="hero-title">BRIGHTMOOR ELECTRICAL<br>COMMUNICATIONS</h1>
  <div class="btn-outline">GET A QUOTE</div>
</section>
<div class="notch-up"></div>

<h2 class="section-title" style="top:378px">OUR GALLERY</h2>
<div class="tile tile-feature" role="img" aria-label="Completed office fit-out with lounge seating, tinted red"></div>
<div class="tile tile-a" role="img" aria-label="Empty warehouse with scissor lift"></div>
<div class="tile tile-b" role="img" aria-label="Steel reinforcement laid for a concrete slab"></div>
<div class="tile tile-c" role="img" aria-label="Warehouse interior with high-bay lighting"></div>
<div class="tile tile-text">Lorem ipsum dolor sit amet, consectetuer adipiscing elit, sed diam nonummy nibh euismod tincidunt ut laoreet dolore magna aliquam erat volutpat.</div>
<div class="tile tile-d" role="img" aria-label="Commercial kitchen with stainless benches and display fridge"></div>

<h2 class="section-title" style="top:669px">OUR SERVICES</h2>

<div class="service" style="left:109px;top:726px">
  <svg width="28" height="28" viewBox="0 0 28 28"><circle cx="14" cy="14" r="13" fill="none" stroke="#ddd"/><circle cx="14" cy="14" r="7" fill="none" stroke="var(--red)" stroke-width="1.6"/><text x="14" y="16.5" font-size="6" text-anchor="middle" fill="var(--red)" font-family="Dosis">24</text></svg>
  24hr Support / faults</div>
<div class="service" style="left:259px;top:726px">
  <svg width="28" height="28" viewBox="0 0 28 28"><circle cx="14" cy="14" r="13" fill="none" stroke="#ddd"/><path d="M14 7a5 5 0 0 0-3 9v2h6v-2a5 5 0 0 0-3-9z M12 20h4" fill="none" stroke="var(--red)" stroke-width="1.5"/></svg>
  Temporary lighting</div>
<div class="service" style="left:419px;top:726px">
  <svg width="28" height="28" viewBox="0 0 28 28"><circle cx="14" cy="14" r="13" fill="none" stroke="#ddd"/><path d="M14 10a4 4 0 0 0-2.5 7v2h5v-2A4 4 0 0 0 14 10z M14 5v2 M7 9l1.5 1 M21 9l-1.5 1 M6 14h2 M20 14h2" fill="none" stroke="var(--red)" stroke-width="1.4"/></svg>
  Energy efficient lighting</div>
<div class="service" style="left:575px;top:726px">
  <svg width="28" height="28" viewBox="0 0 28 28"><circle cx="14" cy="14" r="13" fill="none" stroke="#ddd"/><circle cx="14" cy="14" r="7" fill="var(--red)"/><path d="M14 10c2 2 2 3 1 5-1 1-3 0-2-2" fill="none" stroke="#fff" stroke-width="1.3"/></svg>
  Smoke alarms</div>

<div class="service" style="left:109px;top:811px">
  <svg width="28" height="28" viewBox="0 0 28 28"><circle cx="14" cy="14" r="13" fill="none" stroke="#ddd"/><path d="M8 20l8-8 M15 9l4 4 M9 9l10 10" fill="none" stroke="var(--red)" stroke-width="1.7"/></svg>
  Maintenance</div>
<div class="service" style="left:259px;top:811px">
  <svg width="28" height="28" viewBox="0 0 28 28"><circle cx="14" cy="14" r="13" fill="none" stroke="#ddd"/><rect x="8" y="8" width="12" height="7" fill="none" stroke="var(--red)" stroke-width="1.5"/><path d="M14 15v6" stroke="var(--red)" stroke-width="1.5"/></svg>
  Illuminated signage</div>
<div class="service" style="left:419px;top:811px">
  <svg width="28" height="28" viewBox="0 0 28 28"><circle cx="14" cy="14" r="13" fill="none" stroke="#ddd"/><rect x="8" y="9" width="12" height="10" fill="none" stroke="var(--red)" stroke-width="1.5"/><rect x="11" y="12" width="2" height="4" fill="var(--red)"/><rect x="15" y="12" width="2" height="4" fill="var(--red)"/></svg>
  Switchboard relocations</div>
<div class="service" style="left:575px;top:811px">
  <svg width="28" height="28" viewBox="0 0 28 28"><circle cx="14" cy="14" r="13" fill="none" stroke="#ddd"/><rect x="8" y="10" width="12" height="9" fill="none" stroke="var(--red)" stroke-width="1.5"/><path d="M8 13h12 M11 8v2 M17 8v2" stroke="var(--red)" stroke-width="1.5"/></svg>
  Kitchen / Bathroom</div>

<div class="btn-red">VIEW MORE</div>

<footer class="site-footer"></footer>
<div class="notch-down"></div>

<div class="field" style="left:118px;top:993px;width:119px;height:24px">Name</div>
<div class="field" style="left:240px;top:993px;width:119px;height:24px">Email</div>
<div class="field" style="left:362px;top:993px;width:119px;height:24px">Phone</div>
<div class="field" style="left:118px;top:1019px;width:363px;height:64px">Message</div>
<div class="btn-send">Send</div>

<div class="contact-line" style="top:993px"><svg viewBox="0 0 12 12"><path d="M2 1l2 0 1 3-1.3 1a6 6 0 0 0 3 3L8 7l3 1v2c0 .6-.5 1-1 1C5 11 1 7 1 2c0-.5.4-1 1-1z" fill="#fff"/></svg>0400 555 182</div>
<div class="contact-line" style="top:1014px"><svg viewBox="0 0 12 12"><rect x="3" y="1" width="6" height="10" rx="1" fill="none" stroke="#fff" stroke-width="1.2"/></svg>08 9000 4310</div>
<div class="contact-line" style="top:1035px"><svg viewBox="0 0 12 12"><rect x="1" y="3" width="10" height="7" fill="#fff"/><path d="M1 3l5 4 5-4" fill="none" stroke="#222" stroke-width="1"/></svg>hello@brightmoorelectrical.example</div>
<div class="contact-line" style="top:1057px"><svg viewBox="0 0 12 12"><path d="M6 1a3.5 3.5 0 0 0-3.5 3.5C2.5 7 6 11 6 11s3.5-4 3.5-6.5A3.5 3.5 0 0 0 6 1z" fill="#fff"/><circle cx="6" cy="4.5" r="1.3" fill="#222"/></svg>P.O Box 417 Harbour Point W.A 6999</div>

<div class="social" style="left:515px"></div>
<div class="social" style="left:546px"></div>
<div class="social" style="left:577px"></div>
<div class="social" style="left:608px"></div>

<div class="legal-bar">
  <p class="legal-note">we do not disclose information to third partie'</p>
  <p class="copyright">copyright © 2015 Brightmoor.example</p>
</div>

</body>
</html>
```